GuardPeak website design #1 alarm company in Arizona and California

Alarm company, home security, home protection, video, home automation, smart home, we protect family we the highest quality security products in the market with 24 hour montrioning, also allow family's to control their whole house by being everywhere in the world.

In short, we’re professional, experienced and have the necessary know-how to optimally secure your home or business. Add those skills with our commitment to service and saving you money, and you can’t go wrong trusting

Looking to have a website for current customers and future customers and current employees and future employees to go to. Target current markets listed below get a lot of leads of the website.

Target Market(s)

Arizona and California, Phoenix, Mesa,Gilbert, casa grande, Arizona city, Glendale, peoria, Goodyear, Scottsdale, fountain hills, apache junction, Tempe, surprise, anthem, buckeye, Tucson, Northern California, Modesto, Fresno, Stockton, San Jose, Manteca, Tracy, Sacramento, concord, Southern California, San Bernardino, riverside, Anaheim, Los Angeles, palm desert, Bakersfield

Industry/Entity Type

Security

Coding

Coded - Design and coding required

Number of Pages Required

5+ page

Font styles to use
Sans Serif

Colors
ec1f27
f59296
ffffff
000000
b2b2b2
cacaca
fbd4d5

Requirements
Must have
• A place where a customer can put in the info to get a system(get a free quote),a link to all of my socal media sites, a work for us page, about us page, equipment page, packages page, security page, cameras page, smart home page, support page(FAQ http://www.bluerivenhome.example/faq)somthing like the alomost every answer is right. Partners page.
Nice to have
• Quorvel.example, very nicely done make it look nice like this.
• Bluerivenhome.example
• Pemtra.example
• Kestlo.example
• Wardlyne7.example
• Trellumguard.example
• These are all my favorite sites would love for it to look like this sites.
Should not have
• Need to be clean cut and sharp looking, no unnecessary stuff in it.

```html
<!DOCTYPE html>
<html lang="en">
<head>
<meta charset="utf-8">
<title>GuardPeak – Home Security</title>
<link href="https://fonts.googleapis.com/css2?family=Open+Sans:wght@400;600;700&family=Play:wght@400;700&family=Raleway:wght@700&display=swap" rel="stylesheet">
<style>
:root{
  --red:#ec1f27;
  --red-soft:#f59296;
  --pink:#fbd4d5;
  --white:#ffffff;
  --black:#000000;
  --ink:#222222;
  --text:#333333;
  --muted:#777777;
  --grey:#b2b2b2;
  --grey-2:#cacaca;
  --nav-bg:#f3f3f3;
  --section-bg:#ececec;
  --dark:#111111;
  --footer:#333333;
  --footer-bar:#262626;
  --field:#222222;
}
*{margin:0;padding:0;box-sizing:border-box}
html,body{width:1200px;height:2486px;overflow:hidden}
body{font-family:"Open Sans",Arial,sans-serif;color:var(--text);background:var(--white);position:relative}
.abs{position:absolute}

/* header */
.site-header{position:absolute;left:0;top:0;width:1200px;height:116px}
.brand{position:absolute;left:162px;top:50px;display:flex;align-items:center;gap:12px}
.brand-mark{width:30px;height:30px;background:var(--red)}
.brand-name{font-family:"Open Sans",sans-serif;font-weight:700;font-size:30px;color:var(--red);letter-spacing:.5px}
.call{position:absolute;left:594px;top:46px;display:flex;align-items:center;gap:12px;font-size:23px;color:var(--ink)}
.call-icon{width:34px;height:34px;border-radius:50%;background:var(--red);display:flex;align-items:center;justify-content:center}
.member-login{position:absolute;left:858px;top:46px;width:180px;height:34px;border-radius:17px;background:var(--red);color:var(--white);font-size:14px;display:flex;align-items:center;justify-content:center;gap:7px;text-transform:uppercase}

.main-nav{position:absolute;left:0;top:116px;width:1200px;height:45px;background:var(--nav-bg)}
.main-nav a{position:absolute;top:13px;font-size:12px;color:var(--text);text-decoration:none;transform:translateX(-50%);white-space:nowrap}
.main-nav a.active{color:var(--red);font-weight:600}

/* hero */
.hero{position:absolute;left:0;top:161px;width:1200px;height:449px;background:linear-gradient(90deg,#6a5a52 0%,#4a4440 35%,#3b3c3e 60%,#2f3032 100%)}
.hero-photo{position:absolute;inset:0;background:radial-gradient(ellipse 420px 330px at 300px 190px,rgba(190,150,125,.45),transparent 70%)}
.hero-title{position:absolute;left:592px;top:178px;color:var(--white);font-family:"Raleway","Open Sans",sans-serif;font-weight:700;font-size:21px;line-height:36px;text-transform:uppercase}
.btn-red{position:absolute;background:var(--red);color:var(--white);font-size:14px;display:flex;align-items:center;justify-content:center}
.hero-arrow{position:absolute;top:200px;width:28px;height:52px;border:1.5px solid var(--white);border-radius:14px;display:flex;align-items:center;justify-content:center}

/* about */
.about-photo-frame{position:absolute;left:162px;top:656px;width:287px;height:232px;border:1px solid #dcdcdc;padding:9px;background:var(--white)}
.about-photo{width:100%;height:100%;background:linear-gradient(180deg,#c9d8e6 0%,#a9b7a3 55%,#6f8a44 100%)}
.section-title{font-family:"Play","Open Sans",sans-serif;font-weight:700}
.divider{height:1px;background:#d6d6d6;position:absolute}
.divider-mark{position:absolute;width:10px;height:10px;background:var(--grey)}
.about-text{position:absolute;left:480px;top:712px;width:560px;font-size:12px;line-height:21.5px;color:var(--text)}

/* equipments */
.equipments{position:absolute;left:0;top:933px;width:1200px;height:363px;background:var(--dark)}
.equip-card{position:absolute;top:164px;width:201px;height:133px;border:3px solid var(--white);background:#3a3a3a}
.equip-thumb{position:absolute;inset:0;background:radial-gradient(circle at 50% 50%,#e8e8e8 0%,#9a9a9a 45%,#3a3a3a 75%)}
.equip-label{position:absolute;top:304px;width:201px;text-align:center;color:var(--white);font-weight:700;font-size:14px}

/* features */
.feature{position:absolute;top:1343px;width:181px;text-align:center}
.feature-icon{width:72px;height:72px;border-radius:50%;border:1.5px solid var(--text);margin:0 auto 14px;display:flex;align-items:center;justify-content:center}
.feature-icon.is-active{background:var(--red);border-color:var(--red)}
.feature h3{font-size:13px;font-weight:700;color:var(--ink);margin-bottom:8px}
.feature p{font-size:12px;line-height:16px;color:var(--text)}

/* packages */
.packages{position:absolute;left:0;top:1530px;width:1200px;height:638px;background:var(--section-bg)}
.plan{position:absolute;top:178px;width:219px;height:400px;background:var(--white);text-align:center}
.plan-name{height:57px;padding-top:12px;font-size:18px;line-height:19px;color:var(--ink);border-bottom:1px solid #e2e2e2}
.plan-price{height:70px;display:flex;align-items:center;justify-content:center;gap:14px;border-bottom:1px solid #e2e2e2}
.plan-price strong{font-size:29px;font-weight:700;color:var(--black)}
.plan-price span{font-size:10px;color:var(--muted)}
.plan ul{list-style:none;width:150px;margin:4px auto 0}
.plan li{height:30px;line-height:30px;font-size:10px;color:#8a8a8a;border-bottom:1px solid #e6e6e6}
.plan li:last-child{border-bottom:none}
.plan-buy{position:absolute;left:55px;top:358px;width:105px;height:29px;background:var(--ink);color:var(--white);font-size:10px;display:flex;align-items:center;justify-content:center}
.plan.featured{background:#2b2b2b}
.plan.featured .plan-name{color:var(--white);font-weight:700;border-color:#555}
.plan.featured .plan-price{border-color:#555}
.plan.featured .plan-price strong{color:var(--white)}
.plan.featured .plan-price span{color:#cfcfcf}
.plan.featured li{color:var(--white);border-color:#777}
.plan.featured .plan-buy{background:var(--white);color:var(--ink)}

/* footer */
.site-footer{position:absolute;left:0;top:2168px;width:1200px;height:279px;background:var(--footer);color:var(--white)}
.footer-title{position:absolute;top:42px;font-family:"Play","Open Sans",sans-serif;font-weight:700;font-size:18px;color:var(--white)}
.field{position:absolute;left:162px;width:240px;background:var(--field);color:#cfcfcf;font-size:9px;padding:6px 8px}
.quick-links{position:absolute;left:447px;top:83px;list-style:none}
.quick-links li{font-size:11px;line-height:23.7px;color:var(--white)}
.map{position:absolute;left:626px;top:78px;width:178px;height:156px;background:linear-gradient(135deg,#e6e2c9 0%,#cfd8c0 40%,#9fc0dc 70%,#e9e4cf 100%);border:2px solid var(--white)}
.find-row{position:absolute;left:891px;display:flex;gap:10px;font-size:11px;line-height:14px;color:var(--white)}
.footer-bar{position:absolute;left:0;top:2447px;width:1200px;height:39px;background:var(--footer-bar);color:var(--white)}
.social-dot{position:absolute;top:14px;width:11px;height:11px;border-radius:50%;background:#cfcfcf}
</style>
</head>
<body>

<header class="site-header">
  <div class="brand"><span class="brand-mark"></span><span class="brand-name">GuardPeak</span></div>
  <div class="call">
    <span class="call-icon"><svg width="16" height="16" viewBox="0 0 24 24"><path fill="#fff" d="M6.6 10.8a15 15 0 0 0 6.6 6.6l2.2-2.2c.3-.3.7-.4 1-.2 1.1.4 2.3.6 3.6.6.6 0 1 .4 1 1V20c0 .6-.4 1-1 1A17 17 0 0 1 3 4c0-.6.4-1 1-1h3.5c.6 0 1 .4 1 1 0 1.3.2 2.5.6 3.6.1.3 0 .7-.2 1z"/></svg></span>
    <span>Call: 0198-555-274</span>
  </div>
  <div class="member-login">
    <svg width="12" height="12" viewBox="0 0 24 24"><circle cx="12" cy="7" r="5" fill="#fff"/><path d="M2 23c0-6 4.5-9 10-9s10 3 10 9z" fill="#fff"/></svg>
    Member Login
    <svg width="8" height="10" viewBox="0 0 8 10"><path d="M1 0l6 5-6 5z" fill="#fff"/></svg>
  </div>
</header>

<nav class="main-nav">
  <a class="active" style="left:202px">Home</a>
  <a style="left:293px">About Us</a>
  <a style="left:404px">Work With Us</a>
  <a style="left:522px">Equipment</a>
  <a style="left:623px">Packages</a>
  <a style="left:719px">Security</a>
  <a style="left:823px">Our Camera</a>
  <a style="left:934px">Contact Us</a>
  <svg class="abs" style="left:1008px;top:16px" width="13" height="13" viewBox="0 0 24 24"><circle cx="10" cy="10" r="7" fill="none" stroke="#333" stroke-width="3"/><path d="M15 15l7 7" stroke="#333" stroke-width="3"/></svg>
</nav>

<section class="hero" role="img" aria-label="Photo of a smiling mother hugging her young child at home">
  <div class="hero-photo"></div>
  <div class="hero-arrow" style="left:67px"><svg width="8" height="12" viewBox="0 0 8 12"><path d="M6 1L1 6l5 5" stroke="#fff" stroke-width="1.6" fill="none"/></svg></div>
  <div class="hero-arrow" style="left:1106px"><svg width="8" height="12" viewBox="0 0 8 12"><path d="M2 1l5 5-5 5" stroke="#fff" stroke-width="1.6" fill="none"/></svg></div>
  <h1 class="hero-title">We provided highest quality<br>security your family and business</h1>
  <a class="btn-red" style="left:592px;top:266px;width:149px;height:36px">Read More</a>
</section>

<section class="about">
  <div class="about-photo-frame"><div class="about-photo" role="img" aria-label="Photo of a family of four sitting together on a lawn in front of their house"></div></div>
  <h2 class="section-title abs" style="left:480px;top:648px;font-size:28px;color:var(--ink)">About Us</h2>
  <div class="divider" style="left:480px;top:698px;width:560px"></div>
  <span class="divider-mark" style="left:484px;top:693px"></span>
  <div class="about-text">
    <p>Lorem ipsum dolor sit amet, consectetuer adipiscing elit, sed diam nonummy nibh euismod tincidunt ut laoreet dolore magna aliquam erat volutpat. Ut wisi enim ad minim veniam, quis nostrud exerci tation ullamcorper suscipit lobortis nisl ut aliquip ex ea commodo consequat. Duis autem vel eum iriure dolor in hendrerit in vulputate velitUt wisi enim ad minim veniam, quis nostrud exerci tation ullamcorper suscipit lobortis nisl ut aliquip ex ea commodo consequat.</p>
    <p>Duis autem vel eum iriure dolor in hendrerit in vulputate velitUt wisi enim ad minim veniam.</p>
  </div>
  <a class="btn-red" style="left:480px;top:855px;width:113px;height:33px;border-radius:3px;font-size:13px">Read More</a>
</section>

<section class="equipments">
  <h2 class="section-title abs" style="left:0;width:1200px;text-align:center;top:37px;font-size:27px;color:var(--white)">Our Equipments</h2>
  <span class="divider-mark" style="left:595px;top:78px;background:#666"></span>
  <p class="abs" style="left:0;width:1200px;top:107px;text-align:center;font-size:11.5px;line-height:19px;color:#dcdcdc">Duis aute irure dolor in reprehenderit in voluptate velit esse cillum dolore eu fugiat nulla pariatur. Excepteur sint occaecat cupidatat non proident,<br>sunt in culpa qui officia deserunt mollit anim id est laborum</p>
  <svg class="abs" style="left:130px;top:222px" width="14" height="24" viewBox="0 0 14 24"><path d="M12 1L2 12l10 11" stroke="#fff" stroke-width="2.5" fill="none"/></svg>
  <svg class="abs" style="left:1054px;top:222px" width="14" height="24" viewBox="0 0 14 24"><path d="M2 1l10 11L2 23" stroke="#fff" stroke-width="2.5" fill="none"/></svg>

  <div class="equip-card" style="left:162px"><div class="equip-thumb" role="img" aria-label="White security camera on a wall mount"></div></div>
  <div class="equip-card" style="left:387px"><div class="equip-thumb" role="img" aria-label="White wall-mounted image sensor panel"></div></div>
  <div class="equip-card" style="left:612px"><div class="equip-thumb" role="img" aria-label="Silver video doorbell camera"></div></div>
  <div class="equip-card" style="left:837px"><div class="equip-thumb" role="img" aria-label="White alarm control panel with touch screen"></div></div>
  <div class="equip-label" style="left:162px">Door Camera</div>
  <div class="equip-label" style="left:387px">Img Sensor</div>
  <div class="equip-label" style="left:612px">Bell Camera</div>
  <div class="equip-label" style="left:837px">Voice Recorder</div>
</section>

<section class="features">
  <div class="feature" style="left:148px">
    <div class="feature-icon is-active"><svg width="28" height="32" viewBox="0 0 28 32"><path d="M7 14V9a7 7 0 0 1 14 0v5" stroke="#fff" stroke-width="3.5" fill="none"/><rect x="3" y="14" width="22" height="17" rx="2" fill="#fff"/><rect x="12.5" y="19" width="3" height="7" fill="#ec1f27"/></svg></div>
    <h3>Interactive Security</h3><p>Lorem ipsum dolor sit ametc<br>sed diam nonummy</p>
  </div>
  <div class="feature" style="left:329px">
    <div class="feature-icon"><svg width="28" height="28" viewBox="0 0 28 28"><rect x="2" y="2" width="24" height="24" rx="2" fill="none" stroke="#222" stroke-width="2.5"/><path d="M10 8l10 6-10 6z" fill="#222"/></svg></div>
    <h3>Video Monitoring</h3><p>Lorem ipsum dolor sit ametc<br>sed diam nonummy</p>
  </div>
  <div class="feature" style="left:510px">
    <div class="feature-icon"><svg width="26" height="34" viewBox="0 0 26 34"><path d="M13 2a10 10 0 0 0-6 18v4h12v-4A10 10 0 0 0 13 2z" fill="none" stroke="#222" stroke-width="2.5"/><path d="M8 28h10M9 32h8" stroke="#222" stroke-width="2.5"/></svg></div>
    <h3>Energy Management</h3><p>Lorem ipsum dolor sit ametc<br>sed diam nonummy</p>
  </div>
  <div class="feature" style="left:691px">
    <div class="feature-icon"><svg width="34" height="36" viewBox="0 0 34 36"><circle cx="10" cy="10" r="8" fill="#222"/><circle cx="8" cy="8" r="2.5" fill="#fff"/><path d="M14 14l16 18-3 3-3-3-2 2-2-2 2-2-8-9" fill="#222"/></svg></div>
    <h3>Home Automation</h3><p>Lorem ipsum dolor sit ametc<br>sed diam nonummy</p>
  </div>
  <div class="feature" style="left:872px">
    <div class="feature-icon"><svg width="32" height="30" viewBox="0 0 32 30"><path d="M16 28S2 19 2 10a7 7 0 0 1 14-2 7 7 0 0 1 14 2c0 9-14 18-14 18z" fill="none" stroke="#222" stroke-width="2.5"/><path d="M16 10v10M11 15h10" stroke="#222" stroke-width="2.5"/></svg></div>
    <h3>Wellness</h3><p>Lorem ipsum dolor sit ametc<br>sed diam nonummy</p>
  </div>
</section>

<section class="packages">
  <h2 class="section-title abs" style="left:0;width:1200px;text-align:center;top:38px;font-size:27px;color:var(--ink)">Our <span style="color:var(--red)">Packages</span></h2>
  <span class="divider-mark" style="left:595px;top:80px"></span>
  <p class="abs" style="left:0;width:1200px;top:106px;text-align:center;font-size:11px;line-height:17px;color:var(--text)">Lorem ipsum dolor sit amet, consectetuer adipiscing elit. Suspendisse et justo. Praesent mattis<br>commodo augue. Aliquam ornare hendrerit augue</p>

  <svg class="abs" style="left:568px;top:160px" width="286" height="432" viewBox="0 0 286 432">
    <path d="M28 0H258L286 18H0z" fill="#222"/>
    <path d="M0 416H286L258 432H28z" fill="#222"/>
  </svg>

  <div class="plan" style="left:162px">
    <div class="plan-name">Security<br>Management</div>
    <div class="plan-price"><strong>$89.9</strong><span>/ monthly</span></div>
    <ul><li>touch screen control panel</li><li>3 door/window sensors</li><li>1 motion sensor</li><li>1 keychain remote</li><li>1 yard sign</li><li>3 window decals</li><li>web &amp; mobile control</li></ul>
    <div class="plan-buy">Buy Now</div>
  </div>
  <div class="plan" style="left:381px;border-left:1px solid #e6e6e6">
    <div class="plan-name">Energy<br>Management</div>
    <div class="plan-price"><strong>$90.9</strong><span>/ monthly</span></div>
    <ul><li>touch screen control panel</li><li>1 smart thermostat</li><li>3 door/window sensors</li><li>1 motion sensor</li><li>1 keychain remote</li><li>1 yard sign</li><li>3 window decals</li></ul>
    <div class="plan-buy">Buy Now</div>
  </div>
  <div class="plan featured" style="left:598px">
    <div class="plan-name">Automation<br>Management</div>
    <div class="plan-price"><strong>$99.9</strong><span>/ monthly</span></div>
    <ul><li>touch screen control panel</li><li>1 smart thermostat</li><li>1 door lock</li><li>3 door/window sensors</li><li>1 motion sensor</li><li>1 keychain remote</li><li>1 yard sign</li></ul>
    <div class="plan-buy">Buy Now</div>
  </div>
  <div class="plan" style="left:817px;width:222px">
    <div class="plan-name">Video<br>Monitoring</div>
    <div class="plan-price"><strong>$88.9</strong><span>/ monthly</span></div>
    <ul><li>touch screen control panel</li><li>2 indoor cameras</li><li>3 door/window sensors</li><li>1 motion sensor</li><li>1 keychain remote</li><li>1 yard sign</li><li>3 window decals</li></ul>
    <div class="plan-buy">Buy Now</div>
  </div>
</section>

<footer class="site-footer">
  <h4 class="footer-title" style="left:162px">Get a Free Quote</h4>
  <div class="field" style="top:78px;height:23px">Name</div>
  <div class="field" style="top:110px;height:23px">Email</div>
  <div class="field" style="top:143px;height:53px">Message</div>
  <div class="abs" style="left:162px;top:208px;width:83px;height:25px;background:var(--red);color:#fff;font-size:10px;display:flex;align-items:center;justify-content:center">SEND</div>

  <h4 class="footer-title" style="left:447px">Quick Links</h4>
  <ul class="quick-links"><li>Home</li><li>About Us</li><li>Work With US</li><li>Equipment</li><li>Packages</li><li>Security</li><li>Our Camera</li></ul>

  <h4 class="footer-title" style="left:626px">Location Map</h4>
  <div class="map" role="img" aria-label="Street map showing the office location with a red pin"></div>

  <h4 class="footer-title" style="left:891px">Find Us</h4>
  <div class="find-row" style="top:82px"><svg width="10" height="14" viewBox="0 0 10 14"><path d="M5 0a5 5 0 0 0-5 5c0 4 5 9 5 9s5-5 5-9a5 5 0 0 0-5-5z" fill="#fff"/><circle cx="5" cy="5" r="2" fill="#333"/></svg><span>782 Saguaro Ridge Road<br>Suite 14, Mesa Arizona<br>AZ 85201</span></div>
  <div class="find-row" style="top:140px"><svg width="12" height="12" viewBox="0 0 24 24"><path fill="#fff" d="M6.6 10.8a15 15 0 0 0 6.6 6.6l2.2-2.2c.3-.3.7-.4 1-.2 1.1.4 2.3.6 3.6.6.6 0 1 .4 1 1V20c0 .6-.4 1-1 1A17 17 0 0 1 3 4c0-.6.4-1 1-1h3.5c.6 0 1 .4 1 1 0 1.3.2 2.5.6 3.6.1.3 0 .7-.2 1z"/></svg><span>(480) 555 - 0142</span></div>
  <div class="find-row" style="top:183px"><svg width="12" height="12" viewBox="0 0 12 12"><rect x="1" y="4" width="10" height="7" fill="#fff"/><rect x="3" y="1" width="6" height="3" fill="none" stroke="#fff"/></svg><span>(480) 555 - 0187</span></div>
  <div class="find-row" style="top:226px"><svg width="13" height="10" viewBox="0 0 13 10"><rect x=".5" y=".5" width="12" height="9" fill="none" stroke="#fff"/><path d="M.5.5l6 5 6-5" fill="none" stroke="#fff"/></svg><span>Info@guardpeak.example</span></div>
</footer>

<div class="footer-bar">
  <p class="abs" style="left:162px;top:12px;font-size:10px">Copyright © 2016 &nbsp;GuardPeak. All Right Reserved</p>
  <span class="social-dot" aria-label="Social link" style="left:942px"></span>
  <span class="social-dot" aria-label="Social link" style="left:967px"></span>
  <span class="social-dot" aria-label="Social link" style="left:992px"></span>
  <span class="social-dot" aria-label="Social link" style="left:1026px"></span>
</div>

</body>
</html>
```